依頼詳細
1.ターゲット層は30〜60代の投資家ですが、60代が多めです。

2.グローバルナビ含め、トップページ内のコンテンツは同じですが、各コンテンツの掲載箇所等にこだわりはありませんので自由にデザインして下さい。

3.コンテンツエリアは、2カラム(メイン・右ナビ)で
それぞれのサイズは下記になります。
・メイン:650px
・右ナビ:300px
(メインと右ナビの間が10px)

4.できるだけ幅広いデザインを頂きたいため、
デザインのイメージ等はこちらから指示致しません。
※ご不明点はご質問ください。

5.なおトップロゴは現行のものを利用しますのでデザインの必要ありません。
広告箇所も同じくデザインの必要はありません。
※デザインの必要が無い箇所は添付赤枠部分となります。
※広告はデザインに合わせて配置いたしますので広告箇所をご指定頂く必要はありませ

ご不明な点がありましたら、お気軽にご連絡ください。
サイトURL
http://zerinol.jp/
ページ数
3ページ
希望イメージ
シンプル 複雑
単色 カラフル
暗い 明るい
日常 高級
遊び心 厳粛
未来的 伝統的
女性的 男性的
希望する色
納品ファイル
• イラストレーター形式 (.ai)
• フォトショップ形式 (.psd)
補足説明
基本のフォントサイズも特に指定ございません。

当選者については、アイコンなどになる部分に関して、決定後、切り出しやすいように定義していただきます。

【契約上のご注意】
・採用対象となる方には当社フォーマットの契約書を締結させて頂きます。
※添付「クラウドソーシング向け業務委託契約書_提示締結用.pdf」
【10月21日追記】
提案数が1件しか集まっていないため、募集期間を1週間延長させました。

新期限:10/28

既にご提案頂いた方、当初の期限までにご提案頂く予定だった方は大変申し訳ございません。
もう暫くお待ち下さい。
たくさんのご提案をいただきありがとうございます。
お礼ご返信も間に合っておりませんが、ご返信していないご提案も
全て検討対象とさせて頂きますのでご安心ください。

今後のスケジュールに関しまして追記させて頂きます。
ご提案頂いたデザインを当社上層部に提出し社内検討をさせて頂きます。

上層部スケジュールを合わせて会議を実施・決定の流れになりますので、
日程調整等でもう暫くお時間を頂戴できればと存じます。
■ 選んだ理由

色合いや全体イメージを社内複数人による多数決により決定させていただきました。

■ 提案者全員のお礼・コメント

たくさんのご応募ありがとうございました。
本件につきましては社内調整等、
選定まで時間がかかりましたことお詫びいたします。

また本コンペは3件の当選予定をしておりまして、
今回決定の1件以外に別途2名の方に個別にプロジェクト形式でご発注させていただいております。

```html
<!DOCTYPE html>
<html lang="ja">
<head>
<meta charset="utf-8">
<title>Zerinol 株式情報トップ</title>
<link rel="stylesheet" href="https://fonts.googleapis.com/css2?family=Noto+Sans+JP:wght@400;700&display=swap">
<style>
:root{
  --bg:#e9e9e9;
  --head:#2b2b2b;
  --head2:#444;
  --red:#c8161d;
  --navy:#2c3e5c;
  --line:#cfcfcf;
  --text:#222;
  --sub:#666;
  --link:#1a4a8a;
  --up:#c8161d;
  --down:#1a58b5;
  --panel:#fff;
  --pale:#f4f4f4;
}
*{box-sizing:border-box;margin:0;padding:0}
html,body{width:1200px;height:3000px;overflow:hidden}
body{background:var(--bg);font-family:"Noto Sans JP",sans-serif;color:var(--text);font-size:13px;line-height:1.5;display:flex;flex-direction:column}
.wrap{width:960px;margin:0 auto}
.site-header{background:linear-gradient(#3a3a3a,var(--head));height:120px;color:#fff;flex:none}
.site-header .wrap{display:flex;align-items:center;justify-content:space-between;height:120px}
.brand{display:flex;align-items:center;gap:10px}
.brand-mark{width:30px;height:30px;background:var(--red)}
.brand-name{font-size:28px;font-weight:700;color:#fff}
.brand-url{font-size:11px;color:#bbb;margin-left:4px}
.indices{display:flex;gap:6px}
.index{width:138px;height:78px;background:#1e1e1e;border:1px solid #555;padding:6px 8px}
.index .label{font-size:11px;background:var(--red);padding:0 4px;display:inline-block}
.index .value{font-size:20px;font-weight:700;margin-top:4px;white-space:nowrap}
.index .chg{font-size:11px;color:#ff8a8a;white-space:nowrap}
.global-nav{background:var(--head2);height:40px;border-bottom:3px solid var(--red);flex:none}
.global-nav ul{list-style:none;display:flex;height:37px}
.global-nav li{flex:1;color:#fff;font-size:13px;font-weight:700;text-align:center;line-height:37px;border-right:1px solid #555}
.global-nav li.current{background:var(--red)}
.search-bar{background:#f7f7f7;border-bottom:1px solid var(--line);height:44px;flex:none}
.search-bar .wrap{display:flex;align-items:center;gap:6px;height:44px}
.search-bar input{width:420px;height:26px;border:1px solid #aaa;padding:0 6px;font-family:inherit;font-size:13px}
.btn{display:inline-block;height:26px;padding:0 12px;background:var(--navy);color:#fff;font-size:12px;line-height:26px}
.quick{background:#fff;border-bottom:1px solid var(--line);height:40px;flex:none}
.quick .wrap{display:flex;align-items:center;gap:18px;height:40px;font-size:12px}
.quick .tag{background:var(--red);color:#fff;padding:0 6px;font-weight:700}
.quick a{color:var(--link);text-decoration:none}
.content{display:flex;gap:10px;padding-top:16px;flex:1}
.main{width:650px}
.side{width:300px}
.block{background:var(--panel);border:1px solid var(--line);margin-bottom:18px}
.block-title{display:flex;justify-content:space-between;align-items:center;height:36px;padding:0 10px;border-bottom:2px solid var(--red);font-weight:700;font-size:15px}
.block-title .more{background:var(--navy);color:#fff;font-size:11px;padding:1px 8px;font-weight:400}
.news{list-style:none;padding:8px 10px}
.news li{font-size:12.5px;padding:6px 0;border-bottom:1px dotted #ddd;white-space:nowrap;overflow:hidden;text-overflow:ellipsis}
.news .time{color:var(--sub);margin-right:8px}
.news .mark{display:inline-block;width:12px;height:12px;background:var(--red);margin-right:6px;vertical-align:-1px}
.split{display:flex;gap:10px;padding:10px}
.split .news{flex:1;padding:0;min-width:0}
.mini-chart{width:200px;border:1px solid var(--line);background:var(--pale);flex:none}
.mini-chart .cap{font-size:11px;background:var(--navy);color:#fff;padding:2px 6px}
.ad-slot{background:#dcdcdc;border:1px solid #c6c6c6;display:flex;align-items:center;justify-content:center;color:#999;font-size:12px;margin-bottom:18px}
.tabs{display:flex;gap:2px;padding:10px 10px 0}
.tabs span{font-size:11px;padding:3px 10px;background:#ddd}
.tabs span.on{background:var(--red);color:#fff}
table.rank{width:100%;border-collapse:collapse;font-size:12px}
table.rank th{background:var(--pale);font-weight:400;color:var(--sub);padding:4px 6px;border-bottom:1px solid var(--line);text-align:left}
table.rank td{padding:7px 6px;border-bottom:1px solid #eee}
.num{text-align:right}
.up{color:var(--up)}
.down{color:var(--down)}
.themes{display:grid;grid-template-columns:1fr 1fr;padding:10px;gap:6px 20px;font-size:12.5px}
.themes span::before{content:"";display:inline-block;width:8px;height:8px;background:var(--red);margin-right:8px}
.photo{background:linear-gradient(135deg,#9a9a9a,#3c3c3c);height:250px;margin-bottom:18px;position:relative}
.photo .ad-name{position:absolute;left:10px;bottom:10px;color:#fff;font-weight:700;font-size:14px}
.side .block-title{font-size:14px;border-bottom-color:var(--navy)}
table.idx{width:100%;border-collapse:collapse;font-size:12px}
table.idx td{padding:7px 8px;border-bottom:1px solid #eee}
.promo{height:120px;background:linear-gradient(#fbe3c2,#f3a64b);margin-bottom:18px;display:flex;align-items:center;justify-content:center;font-weight:700;font-size:22px;color:var(--red)}
.site-footer{background:#fff;border-top:3px solid var(--red);padding:16px 0 0;font-size:11px;color:var(--sub);flex:none}
.site-footer .links{margin:8px 0;color:var(--link)}
.site-footer .copy{text-align:center;background:var(--head);color:#ccc;padding:8px 0;margin-top:10px}
</style>
</head>
<body>
<header class="site-header">
  <div class="wrap">
    <div class="brand"><span class="brand-mark"></span><span class="brand-name">Zerinol</span><span class="brand-url">zerinol.jp</span></div>
    <div class="indices">
      <div class="index"><span class="label">ZR225</span><div class="value">15,318.22</div><div class="chg">+42.11 (+0.27%)</div></div>
      <div class="index"><span class="label">ドル円</span><div class="value">107.84</div><div class="chg">+0.22 (+0.20%)</div></div>
      <div class="index"><span class="label">新興指数</span><div class="value">2,238.74</div><div class="chg">+8.40 (+0.37%)</div></div>
      <div class="index"><span class="label">為替ゲージ</span><div class="value">965.71</div><div class="chg">-1.23 (-0.12%)</div></div>
    </div>
  </div>
</header>
<nav class="global-nav"><div class="wrap"><ul>
  <li class="current">トップ</li><li>市場ニュース</li><li>決算速報</li><li>株価注意報</li><li>銘柄探検</li><li>会社情報</li><li>市場マップ</li><li>ランキング</li>
</ul></div></nav>
<div class="search-bar"><div class="wrap"><input type="text" value="銘柄名・コード"><span class="btn">株価</span><span class="btn">ニュース</span></div></div>
<div class="quick"><div class="wrap"><span class="tag">注目</span><a>決算カレンダー</a><a>ストップ高</a><a>年初来高値</a><a>出来高急増</a><a>テーマ株</a><a>IPO情報</a></div></div>

<div class="wrap content">
  <main class="main">
    <section class="block">
      <h2 class="block-title">TOP NEWS<span class="more">ニュース一覧</span></h2>
      <div class="split">
        <ul class="news">
          <li><span class="mark"></span>ZR225は続伸、主力株に買い戻し広がる</li>
          <li><span class="mark"></span>【特集】株価急伸の3銘柄、業績上振れに注目</li>
          <li><span class="mark"></span>本日の【ストップ高】銘柄一覧（前場）</li>
          <li><span class="mark"></span>東陽機工が反発、受注回復観測を好感</li>
          <li><span class="mark"></span>【材料】ソラネットが続伸、新サービス発表</li>
          <li><span class="mark"></span>ドル円は107円台後半で小動き</li>
          <li><span class="mark"></span>新興市場は小幅高、IPO銘柄に物色</li>
          <li><span class="mark"></span>今週の決算発表予定と注目ポイント</li>
          <li><span class="mark"></span>明日の【好悪材料】を先取り</li>
        </ul>
        <div class="mini-chart"><div class="cap">ZR225 5分足</div>
          <svg width="198" height="200" viewBox="0 0 198 200"><polyline fill="none" stroke="#c8161d" stroke-width="2" points="5,150 25,136 45,142 65,108 85,116 105,82 125,96 145,68 165,76 190,54"/><line x1="0" y1="176" x2="198" y2="176" stroke="#ccc"/></svg>
        </div>
      </div>
    </section>
    <div class="ad-slot" style="height:70px">広告</div>

    <section class="block">
      <h2 class="block-title">決算速報<span class="more">決算速報一覧</span></h2>
      <div class="split">
        <ul class="news">
          <li><span class="time">10/28 15:30</span>ミナトデータ、上期経常は2%上振れ</li>
          <li><span class="time">10/28 15:10</span>北星電機、4-9月期税引前は減益着地</li>
          <li><span class="time">10/28 15:00</span>ハルモ、今期経常を7%上方修正</li>
          <li><span class="time">10/28 14:30</span>遊星堂、上期最終は赤字縮小</li>
          <li><span class="time">10/28 14:00</span>東陽機工、7-9月期は増収増益</li>
          <li><span class="time">10/28 13:30</span>ソラネット、通期予想を据え置き</li>
          <li><span class="time">10/28 13:00</span>北浜化成、配当予想を増額修正</li>
        </ul>
        <div class="mini-chart"><div class="cap">決算発表件数</div>
          <svg width="198" height="180" viewBox="0 0 198 180"><g fill="#2c3e5c"><rect x="12" y="100" width="20" height="70"/><rect x="42" y="78" width="20" height="92"/><rect x="72" y="52" width="20" height="118"/><rect x="102" y="90" width="20" height="80"/><rect x="132" y="38" width="20" height="132"/><rect x="162" y="64" width="20" height="106"/></g></svg>
        </div>
      </div>
    </section>
    <div class="ad-slot" style="height:120px">広告</div>

    <section class="block">
      <h2 class="block-title">ランキング・市況指標<span class="more">ランキング一覧</span></h2>
      <div class="tabs"><span class="on">値上がり率</span><span>値下がり率</span><span>出来高</span><span>売買代金</span><span>ストップ高</span></div>
      <div class="split">
        <table class="rank" style="flex:1">
          <tr><th>順位</th><th>コード</th><th>銘柄</th><th class="num">株価</th><th class="num">前日比</th></tr>
          <tr><td>1</td><td>4321</td><td>ミナトデータ</td><td class="num">1,232</td><td class="num up">+150</td></tr>
          <tr><td>2</td><td>6602</td><td>北星電機</td><td class="num">548</td><td class="num up">+64</td></tr>
          <tr><td>3</td><td>8136</td><td>ハルモ</td><td class="num">4,205</td><td class="num up">+420</td></tr>
          <tr><td>4</td><td>9434</td><td>ソラネット</td><td class="num">2,462</td><td class="num up">+196</td></tr>
          <tr><td>5</td><td>6954</td><td>東陽機工</td><td class="num">18,900</td><td class="num up">+1,230</td></tr>
        </table>
        <div class="mini-chart"><div class="cap">騰落レシオ</div>
          <svg width="198" height="160" viewBox="0 0 198 160"><polyline fill="none" stroke="#1a58b5" stroke-width="2" points="5,120 30,94 55,104 80,68 105,80 130,54 155,64 190,40"/></svg>
        </div>
      </div>
    </section>

    <section class="block">
      <h2 class="block-title">人気ニュース【ベスト10】<span class="more">ベスト10を見る</span></h2>
      <ul class="news">
        <li>1. 本日の【ストップ高】銘柄一覧（後場）</li>
        <li>2. 【特集】年末高に乗る、出遅れ好業績株</li>
        <li>3. ミナトデータが急伸、上期上振れを好感</li>
        <li>4. 明日の株式相場見通し＝押し目買い優勢</li>
        <li>5. 【材料】遊星堂が新型機の発売日を発表</li>
        <li>6. 北星電機、通期見通しを下方修正</li>
        <li>7. 新興市場の注目IPO、初値は公開価格超え</li>
        <li>8. 今週の【早わかり】株式市況</li>
        <li>9. ハルモが続伸、海外販売が好調</li>
        <li>10. 主市場の出来高、今年最低水準に</li>
      </ul>
    </section>

    <section class="block">
      <h2 class="block-title">人気テーマ<span class="more">ベスト30を見る</span></h2>
      <div class="themes">
        <span>1. 人工知能</span><span>6. 燃料電池</span>
        <span>2. 円安メリット</span><span>7. 再生医療</span>
        <span>3. 五輪関連</span><span>8. 自動運転</span>
        <span>4. リニア新幹線</span><span>9. 防衛関連</span>
        <span>5. スマホゲーム</span><span>10. 量子通信</span>
      </div>
    </section>

    <section class="block">
      <h2 class="block-title">人気ニュース（市場別）<span class="more">ニュース一覧</span></h2>
      <ul class="news">
        <li>主市場：主力輸出株に買い、円安が追い風</li>
        <li>第二市場：材料株の循環物色が続く</li>
        <li>新興市場：バイオ関連に利益確定売り</li>
        <li>先物：ZR225先物は小幅続伸</li>
        <li>為替：ドル円は107円80銭近辺</li>
        <li>海外：米国株は高安まちまち</li>
        <li>商品：原油先物は反落</li>
      </ul>
    </section>

    <section class="block">
      <h2 class="block-title">開示情報<span class="more">開示一覧</span></h2>
      <ul class="news">
        <li><span class="time">10/28 17:00</span>ミナトデータ　業績予想の修正に関するお知らせ</li>
        <li><span class="time">10/28 16:30</span>北星電機　剰余金の配当に関するお知らせ</li>
        <li><span class="time">10/28 16:00</span>ハルモ　自己株式取得に係る事項の決定</li>
        <li><span class="time">10/28 15:45</span>東陽機工　決算短信〔日本基準〕（連結）</li>
        <li><span class="time">10/28 15:30</span>遊星堂　新製品発売に関するお知らせ</li>
        <li><span class="time">10/28 15:00</span>ソラネット　組織変更に関するお知らせ</li>
      </ul>
    </section>
  </main>

  <aside class="side">
    <div class="photo" role="img" aria-label="自動車広告の写真"><span class="ad-name">Auron SX</span></div>
    <section class="block">
      <h2 class="block-title">ZR225<span class="more">詳細</span></h2>
      <svg width="298" height="170" viewBox="0 0 298 170"><rect width="298" height="170" fill="#f4f4f4"/><polyline fill="none" stroke="#c8161d" stroke-width="2" points="10,136 40,124 70,130 100,102 130,108 160,80 190,88 220,62 250,68 288,46"/></svg>
    </section>
    <section class="block">
      <h2 class="block-title">主要指標<span class="more">一覧</span></h2>
      <table class="idx">
        <tr><td>ZR225</td><td class="num">15,318.22</td><td class="num up">+42.11</td></tr>
        <tr><td>ZR総合</td><td class="num">1,264.31</td><td class="num up">+3.80</td></tr>
        <tr><td>新興指数</td><td class="num">2,238.74</td><td class="num up">+8.40</td></tr>
        <tr><td>グロース指数</td><td class="num">965.71</td><td class="num down">-1.23</td></tr>
        <tr><td>ドル円</td><td class="num">107.84</td><td class="num up">+0.22</td></tr>
        <tr><td>ユーロ円</td><td class="num">136.02</td><td class="num down">-0.15</td></tr>
        <tr><td>米国30種</td><td class="num">16,805.41</td><td class="num up">+12.53</td></tr>
      </table>
    </section>
    <div class="promo">決算速報</div>
    <div class="ad-slot" style="height:260px">広告</div>
    <div class="ad-slot" style="height:260px">広告</div>
  </aside>
</div>

<footer class="site-footer">
  <div class="wrap">
    <p>当サイトの情報は投資判断の参考として提供するもので、投資勧誘を目的としたものではありません。最終的な投資判断はご自身でお願いいたします。</p>
    <p class="links">利用規約 ｜ 個人情報保護方針 ｜ 会社概要 ｜ 広告掲載 ｜ お問い合わせ ｜ サイトマップ</p>
  </div>
  <div class="copy">© Zerinol Co., Ltd. All rights reserved.</div>
</footer>
</body>
</html>
```